Need a flyer for new tech startup

We are developing a new app that helps business owners streamline their efficiency when it comes to wages. The software is called PayVexa and it is composed of dashboards and reports on how the user's business and employees are performing.

We want a flyer created that is clean, smart, techy and fun. There should be placeholder text for title, h1, h2, body, call to action (sign up), etc. Images, backgrounds, transitions and breaks should also be present.

You can visit our website, payvexa.net, but I don't want too much taken from what we have online. We will likely be taking elements from this project and putting them on our website to better establish the branding.

Bonus points for the incorporation or play on light, lightbulb, darkness, etc. ;)

***Final deliverable must include a PSD file with individual layers. Thanks so much!

Tag words to describe our brand: streamline, efficiency, clockwork, profitability, reports, charts, dashboard, feedback, lightbulb, intelligence

Here is the UI that the back end of our software uses: https://demo.tilemorrow.net/plintakit-html-pro/index.html

```html
<!DOCTYPE html>
<html lang="en">
<head>
<meta charset="UTF-8">
<title>PayVexa Flyer</title>
<link href="https://fonts.googleapis.com/css2?family=Oswald:wght@500;600&family=Montserrat:wght@400;500;600;700&display=swap" rel="stylesheet">
<style>
  :root {
    --navy: #1b2d6b;
    --blue: #1f5fbf;
    --blue-deep: #12357f;
    --yellow: #e6ab12;
    --yellow-soft: #f5c842;
    --paper: #ececec;
    --white: #ffffff;
    --ink: #1e1e1e;
    --line: #d9d9d9;
  }
  * { box-sizing: border-box; margin: 0; padding: 0; }
  html, body { width: 800px; height: 1200px; overflow: hidden; background: var(--white); }
  body { font-family: "Montserrat", sans-serif; color: var(--ink); }

  .flyer { position: relative; width: 800px; height: 1200px; overflow: hidden; background: var(--white); }

  /* Hero */
  .hero { position: absolute; inset: 0 0 auto 0; height: 520px; background: var(--paper); overflow: hidden; }
  .hero-blob { position: absolute; inset: 0; }
  .brand { position: absolute; left: 45px; top: 66px; display: flex; align-items: center; gap: 12px; }
  .brand-dot { width: 22px; height: 22px; border-radius: 50%; background: var(--yellow); }
  .brand-name { font-weight: 700; font-size: 46px; color: var(--navy); letter-spacing: -0.5px; }

  .headline { position: absolute; left: 45px; top: 180px; font-family: "Oswald", sans-serif; font-weight: 600; line-height: 1.04; color: var(--navy); }
  .headline .line { display: block; font-size: 44px; letter-spacing: 0.5px; }
  .headline .accent { display: block; font-size: 72px; color: var(--yellow); margin-top: 2px; }
  .headline-rule { position: absolute; left: 45px; top: 392px; width: 56px; height: 4px; background: var(--yellow); }
  .hero-intro { position: absolute; left: 45px; top: 425px; width: 315px; font-size: 12.5px; font-weight: 700; line-height: 1.3; color: var(--ink); }

  .hero-art { position: absolute; left: 420px; top: 175px; width: 345px; height: 290px; border-radius: 22px;
    background: linear-gradient(160deg, var(--yellow-soft) 0%, var(--yellow) 100%); }

  /* Content */
  .content { position: absolute; top: 520px; left: 0; width: 800px; height: 420px; background: var(--white); }
  .col-divider { position: absolute; left: 403px; top: 22px; width: 1px; height: 380px; background: var(--line); }
  .col-left { position: absolute; left: 45px; top: 22px; width: 340px; }
  .col-right { position: absolute; left: 432px; top: 22px; width: 330px; }

  .topic { margin-bottom: 22px; }
  .topic-head { display: flex; align-items: center; gap: 8px; margin-bottom: 10px; }
  .topic-icon { width: 26px; height: 26px; flex: none; }
  .topic-title { font-size: 12.5px; font-weight: 700; color: var(--navy); line-height: 1.15; text-transform: uppercase; letter-spacing: 0.2px; }
  .topic-title .hl { color: var(--yellow); }
  .topic-body { font-size: 11.6px; line-height: 1.32; text-align: justify; color: #333; }

  .feature-title { font-size: 15px; font-weight: 700; color: var(--navy); line-height: 1.15; text-transform: uppercase; letter-spacing: 0.3px; }
  .feature-title .hl { display: block; color: var(--yellow); }
  .feature-lead { font-size: 11.6px; font-weight: 700; margin: 16px 0 14px; }
  .team-photo { margin-top: 16px; width: 325px; height: 200px;
    background: linear-gradient(180deg, #b9c7d8 0%, #b9c7d8 18%, #2b5cc9 30%, #2452bb 68%, #b8a583 80%, #8c7c64 100%);
    box-shadow: 8px 8px 0 -6px var(--yellow); }

  /* Features */
  .features { position: absolute; top: 940px; left: 0; width: 800px; height: 190px; background: var(--paper); }
  .features-tab { position: absolute; left: 0; top: 0; width: 230px; height: 36px; background: var(--blue); clip-path: polygon(0 0, 100% 0, 90% 100%, 0 100%);
    font-weight: 700; font-size: 18px; color: var(--white); padding: 7px 0 0 44px; letter-spacing: 0.3px; }
  .features-tab .hl { color: var(--yellow); }
  .feature-list { position: absolute; left: 45px; top: 58px; display: grid; grid-template-columns: 198px 180px 160px; row-gap: 14px; list-style: none; }
  .feature-list li { display: flex; gap: 8px; font-size: 11.5px; font-weight: 500; color: var(--navy); line-height: 1.25; }
  .tick { width: 13px; height: 13px; flex: none; margin-top: 1px; }
  .apps-label { position: absolute; left: 617px; top: 40px; font-size: 10.5px; font-weight: 600; color: var(--navy); letter-spacing: 0.3px; }

  .apps-screen { position: absolute; left: 590px; top: 1035px; width: 190px; height: 138px; z-index: 2;
    background: #f4f6fa; border: 5px solid #222; border-bottom-width: 8px; border-radius: 5px; }
  .apps-screen svg { display: block; }
  .apps-base { position: absolute; left: 575px; top: 1172px; width: 220px; height: 7px; z-index: 2; background: #c9ccd2; border-radius: 0 0 6px 6px; }

  /* Call to action */
  .cta-rule { position: absolute; top: 1130px; left: 0; width: 800px; height: 6px; background: var(--navy); }
  .cta { position: absolute; top: 1136px; left: 0; width: 800px; height: 64px; background: var(--yellow); display: flex; align-items: center; padding-left: 45px; gap: 16px; color: var(--white); }
  .cta-label { font-size: 17px; font-weight: 500; }
  .cta-phone { font-size: 28px; font-weight: 700; letter-spacing: 0.5px; }
  .cta-web { display: flex; align-items: center; gap: 8px; font-size: 16px; font-weight: 600; }
</style>
</head>
<body>
<main class="flyer">

  <section class="hero">
    <svg class="hero-blob" width="800" height="520" viewBox="0 0 800 520" aria-hidden="true">
      <defs>
        <linearGradient id="blobFill" x1="0" y1="0" x2="1" y2="1">
          <stop offset="0" stop-color="#1b2d6b"/>
          <stop offset="1" stop-color="#1f5fbf"/>
        </linearGradient>
      </defs>
      <path d="M330 0 C395 8 405 45 398 100 C392 150 388 200 420 235 C470 258 500 300 440 330 C400 352 410 420 470 455 C560 505 690 470 800 430 L800 0 Z" fill="url(#blobFill)" stroke="#e6ab12" stroke-width="5"/>
      <line x1="440" y1="130" x2="490" y2="130" stroke="#5fb0f2" stroke-width="5" stroke-linecap="round"/>
      <rect x="700" y="105" width="36" height="36" rx="5" fill="#2f7fe0"/>
      <rect x="762" y="118" width="8" height="8" fill="#5fb0f2"/>
      <circle cx="410" cy="168" r="13" fill="#2f5fc7" stroke="#ececec" stroke-width="3"/>
    </svg>

    <div class="brand">
      <span class="brand-name">PayVexa</span>
      <span class="brand-dot"></span>
    </div>

    <h1 class="headline">
      <span class="line">MANAGE YOUR</span>
      <span class="line">SERVICE BUSINESS</span>
      <span class="accent">SMARTER!</span>
    </h1>
    <div class="headline-rule"></div>
    <p class="hero-intro">It's time to turn on the lights, and that's why we came up with PayVexa, your real-time, deep-dive dashboard for the financial health of your service business.</p>

    <div class="hero-art" role="img" aria-label="Illustration of a large glowing lightbulb with a team of people around it, one on a ladder"></div>
  </section>

  <section class="content">
    <div class="col-left">
      <article class="topic">
        <div class="topic-head">
          <svg class="topic-icon" viewBox="0 0 26 26" aria-hidden="true"><rect x="4" y="3" width="18" height="20" rx="2" fill="none" stroke="#7fb2e8" stroke-width="1.6"/><path d="M8 17 L12 12 L15 15 L19 9" fill="none" stroke="#7fb2e8" stroke-width="1.6"/></svg>
          <h2 class="topic-title">Spot trends before<br><span class="hl">they're a problem</span></h2>
        </div>
        <p class="topic-body">PayVexa gives your business and employee feedback that analyzes marginal changes that could be the start of a negative pattern. Quickly isolate the potential issue and deal with it so you mitigate your liabilities.</p>
      </article>

      <article class="topic">
        <div class="topic-head">
          <svg class="topic-icon" viewBox="0 0 26 26" aria-hidden="true"><path d="M4 19 L6 8 L10 13 L13 6 L16 13 L20 8 L22 19 Z" fill="none" stroke="#7fb2e8" stroke-width="1.6"/><line x1="4" y1="22" x2="22" y2="22" stroke="#7fb2e8" stroke-width="1.6"/></svg>
          <h2 class="topic-title">Not all employees are<br><span class="hl">created equal</span></h2>
        </div>
        <p class="topic-body">Wouldn't it be great if you knew who on your team was overpaid and who was underpaid? Who is most productive and least productive? Who is improving and who is deteriorating? Identify and reward your rock-</p>
      </article>

      <article class="topic">
        <div class="topic-head">
          <svg class="topic-icon" viewBox="0 0 26 26" aria-hidden="true"><rect x="3" y="5" width="20" height="14" rx="2" fill="none" stroke="#7fb2e8" stroke-width="1.6"/><line x1="9" y1="22" x2="17" y2="22" stroke="#7fb2e8" stroke-width="1.6"/><line x1="7" y1="10" x2="14" y2="10" stroke="#7fb2e8" stroke-width="1.6"/><line x1="7" y1="14" x2="18" y2="14" stroke="#7fb2e8" stroke-width="1.6"/></svg>
          <h2 class="topic-title">A dashboard <span class="hl">on steroids</span></h2>
        </div>
        <p class="topic-body">Turn the lights on! Running a service business can be chaotic and you often have to make quick choices. You can't wait for your accounting statements to come back in order to make timely decisions. PayVexa brings new light to the managing by giving a real-time dashboard and reports on your employee's and business' performance.</p>
      </article>
    </div>

    <div class="col-divider"></div>

    <div class="col-right">
      <h2 class="feature-title">Paying employees by<span class="hl">commission sucks!</span></h2>
      <p class="feature-lead">The next generation of compensation.</p>
      <p class="topic-body">PayVexa is a much better way to compensate that is ultimately more fair, efficient, transparent and motivating! Not to mention, paying by commission only can easily become illegal if you're not properly accounting for OT, Employment Insurance, Breaks, and minimum wages.</p>
      <div class="team-photo" role="img" aria-label="Photo of a service team in matching blue sweatshirts standing in front of a work van"></div>
    </div>
  </section>

  <section class="features">
    <div class="features-tab">OUR <span class="hl">FEATURES</span></div>
    <ul class="feature-list">
      <li><svg class="tick" viewBox="0 0 14 14" aria-hidden="true"><circle cx="7" cy="7" r="6" fill="none" stroke="#1b2d6b" stroke-width="1.2"/><path d="M4 7.2 L6.2 9.3 L10 4.8" fill="none" stroke="#1b2d6b" stroke-width="1.3"/></svg>Employee Feedback</li>
      <li><svg class="tick" viewBox="0 0 14 14" aria-hidden="true"><circle cx="7" cy="7" r="6" fill="none" stroke="#1b2d6b" stroke-width="1.2"/><path d="M4 7.2 L6.2 9.3 L10 4.8" fill="none" stroke="#1b2d6b" stroke-width="1.3"/></svg>Crew Combo</li>
      <li><svg class="tick" viewBox="0 0 14 14" aria-hidden="true"><circle cx="7" cy="7" r="6" fill="none" stroke="#1b2d6b" stroke-width="1.2"/><path d="M4 7.2 L6.2 9.3 L10 4.8" fill="none" stroke="#1b2d6b" stroke-width="1.3"/></svg>Deep Dive Reports</li>
      <li><svg class="tick" viewBox="0 0 14 14" aria-hidden="true"><circle cx="7" cy="7" r="6" fill="none" stroke="#1b2d6b" stroke-width="1.2"/><path d="M4 7.2 L6.2 9.3 L10 4.8" fill="none" stroke="#1b2d6b" stroke-width="1.3"/></svg>Gamification &amp; Incentive<br>Deployment</li>
      <li><svg class="tick" viewBox="0 0 14 14" aria-hidden="true"><circle cx="7" cy="7" r="6" fill="none" stroke="#1b2d6b" stroke-width="1.2"/><path d="M4 7.2 L6.2 9.3 L10 4.8" fill="none" stroke="#1b2d6b" stroke-width="1.3"/></svg>Timesheets Are Done!</li>
      <li><svg class="tick" viewBox="0 0 14 14" aria-hidden="true"><circle cx="7" cy="7" r="6" fill="none" stroke="#1b2d6b" stroke-width="1.2"/><path d="M4 7.2 L6.2 9.3 L10 4.8" fill="none" stroke="#1b2d6b" stroke-width="1.3"/></svg>Cash Is King!</li>
    </ul>
    <p class="apps-label">APPS SCREENSHOTS</p>
  </section>

  <div class="cta-rule"></div>
  <footer class="cta">
    <span class="cta-label">CALL US NOW: <span class="cta-phone">0198765432</span></span>
    <span class="cta-web">
      <svg width="16" height="16" viewBox="0 0 16 16" aria-hidden="true"><circle cx="8" cy="8" r="6.5" fill="none" stroke="#fff" stroke-width="1.4"/><ellipse cx="8" cy="8" rx="3" ry="6.5" fill="none" stroke="#fff" stroke-width="1.2"/><line x1="1.5" y1="8" x2="14.5" y2="8" stroke="#fff" stroke-width="1.2"/></svg>
      www.payvexa.net
    </span>
  </footer>

  <div class="apps-screen" role="img" aria-label="App dashboard with a line chart and data tables">
    <svg width="180" height="125" viewBox="0 0 180 125" aria-hidden="true">
      <rect x="0" y="0" width="180" height="10" fill="#ffffff"/>
      <rect x="6" y="3" width="24" height="4" rx="2" fill="#c5cbd6"/>
      <rect x="150" y="3" width="22" height="4" rx="2" fill="#5fb0f2"/>
      <rect x="0" y="10" width="28" height="115" fill="#ffffff"/>
      <rect x="5" y="18" width="18" height="3" fill="#d3d8e0"/>
      <rect x="5" y="26" width="15" height="3" fill="#d3d8e0"/>
      <rect x="5" y="34" width="18" height="3" fill="#d3d8e0"/>
      <rect x="5" y="42" width="13" height="3" fill="#d3d8e0"/>
      <rect x="5" y="50" width="17" height="3" fill="#d3d8e0"/>
      <rect x="34" y="16" width="140" height="52" rx="2" fill="#ffffff"/>
      <polyline points="40,58 58,50 74,54 92,40 110,46 128,30 146,36 168,22" fill="none" stroke="#3d8fe0" stroke-width="1.5"/>
      <polyline points="40,62 58,58 74,60 92,52 110,55 128,46 146,50 168,42" fill="none" stroke="#7fd3c2" stroke-width="1.2"/>
      <rect x="34" y="74" width="67" height="45" rx="2" fill="#ffffff"/>
      <rect x="107" y="74" width="67" height="45" rx="2" fill="#ffffff"/>
      <rect x="40" y="81" width="50" height="3" fill="#d3d8e0"/>
      <rect x="40" y="90" width="40" height="3" fill="#d3d8e0"/>
      <rect x="40" y="99" width="48" height="3" fill="#d3d8e0"/>
      <rect x="40" y="108" width="36" height="3" fill="#d3d8e0"/>
      <rect x="113" y="81" width="50" height="3" fill="#d3d8e0"/>
      <rect x="113" y="90" width="44" height="3" fill="#d3d8e0"/>
      <rect x="113" y="99" width="52" height="3" fill="#d3d8e0"/>
      <rect x="113" y="108" width="38" height="3" fill="#d3d8e0"/>
    </svg>
  </div>
  <div class="apps-base"></div>

</main>
</body>
</html>
```